Investment Management Firm Power point template

Harrowgate Capital is a real estate investment firm focused on buying commercial office and residential property in the UK. We produce powerpoint presentations for our Board of Directors, Investment Committee and also to external investors.

We are looking for a powerpoint design template which we can use for future presentations which provide a professional look and feel.

Our current website: http://www.harrowgatecapital.co.uk/

Target Market(s)

Institution Investors, Board of Directors, Professionals

Industry/Entity Type

Real Estate

Requirements
Must have
• Leverage off the current logo and colour scheme. However, does not have to purely rely on this colour scheme.
• - Title page
• - Content Page
• - Slide where graphs can be incorporated
• - Slide where photos can be incorporated
• - Slide of UK Map which can show where the property portfolio is currently located
• - Other slides incorporating smart art or other designs that can be used for future presentations
Nice to have
• An example of graphics that we would love to have in the powerpoint pack which we can easily edit has been attached

```html
<!DOCTYPE html>
<html lang="en">
<head>
<meta charset="utf-8">
<title>Harrowgate Capital – Presentation Template</title>
<link href="https://fonts.googleapis.com/css2?family=Titillium+Web:wght@400;600;700&display=swap" rel="stylesheet">
<style>
:root{
  --navy:#345a7a;
  --navy-dark:#1d4e6e;
  --ink:#3a3a3a;
  --text:#555a60;
  --bar:#29b6e8;
  --bar-label:#1a8fc4;
  --footer:#333536;
  --page:#f4f5f6;
  --black:#000;
  --disc:#1b1b1b;
  --grey-band:#5a5b5d;
  --grey-band-light:#a9abad;
  --red:#e0212e;
  --green:#6cc04a;
  --orange:#f07e26;
  --gold:#e8b923;
}
*{margin:0;padding:0;box-sizing:border-box}
html,body{width:1039px;height:1200px;overflow:hidden;background:var(--black)}
body{font-family:"Titillium Web",Arial,sans-serif;color:var(--text)}
.stage{position:relative;width:1122px;height:1296px;transform:scale(0.926);transform-origin:0 0;background:var(--black)}
.slide{position:absolute;width:520px;height:389px;overflow:hidden;
  background:radial-gradient(ellipse at 50% 0%,#e9ebed 0%,var(--page) 45%,#fafafa 100%)}
.slide.tall{height:390px}
.slide::after{content:"";position:absolute;left:0;right:0;bottom:0;height:16px;background:var(--footer)}
.s1{left:24px;top:30px}.s2{left:572px;top:30px}
.s3{left:24px;top:446px}.s4{left:572px;top:446px}
.s5{left:24px;top:858px}.s6{left:572px;top:858px}
.abs{position:absolute}

.cover-band{position:absolute;left:0;top:0;width:100%;height:207px;background:var(--navy);text-align:center;color:#fff}
.cover-title{margin-top:110px;font-size:25px;font-weight:700;line-height:30px}
.cover-sub{margin:6px auto 0;width:300px;font-size:10.5px;line-height:16px;color:#dbe4ec}
.brand{position:absolute;left:135px;top:266px;display:flex;align-items:center;gap:10px}
.brand-square{width:37px;height:37px;background:var(--navy)}
.brand-name{font-size:29px;font-weight:400;color:var(--ink);letter-spacing:-.3px}

.slide-title{position:absolute;left:0;width:100%;top:10px;text-align:center;font-size:18px;font-weight:600;color:var(--navy-dark)}
.slide-title span{display:inline-block;padding:0 20px 1px;border-bottom:1px solid var(--navy-dark);line-height:22px}

.item{position:absolute;left:18px;display:flex;gap:13px}
.item-icon{flex:none;width:17px;height:17px;margin-top:3px;background:var(--navy)}
.item h3{font-size:12.5px;font-weight:600;color:var(--navy-dark);line-height:16px}
.item p{font-size:10.5px;line-height:15.6px;color:var(--text)}
.item p+p{margin-top:15px}

.photo{position:absolute}
.photo-towers{left:294px;top:60px;width:226px;height:302px;background:linear-gradient(160deg,#dfe8f7 0%,#7fa0e6 35%,#2f55c9 65%,#1b2f7a 100%)}
.photo-river{left:0;top:114px;width:277px;height:217px;background:linear-gradient(180deg,#6b7a8c 0%,#c9a871 38%,#7a6a55 55%,#4d4a45 75%,#8c8070 100%)}

.image-band{position:absolute;left:0;top:86px;width:277px;height:26px;background:var(--grey-band);color:#fff;text-align:right;padding-right:8px;font-size:14px;font-weight:600;line-height:26px}
.image-band.light{background:var(--grey-band-light)}
.column{position:absolute;left:289px;top:86px;width:200px;font-size:8.6px;line-height:13px;color:var(--text)}
.column p+p{margin-top:13px}

.header-band{position:absolute;left:0;top:0;width:100%;height:38px;background:var(--navy);color:#fff;font-size:17px;font-weight:600;line-height:38px;padding-left:11px}

.chart-label{font-family:"Titillium Web",Arial,sans-serif}
.return{position:absolute;top:281px;width:80px;height:80px;border-radius:50%;background:var(--disc);color:#fff;text-align:center}
.return-name{position:absolute;left:0;right:0;top:6px;font-size:6px;font-weight:700;text-transform:uppercase;line-height:7px}
.return-value{position:absolute;left:0;right:0;top:27px;font-size:20px;font-weight:700;line-height:24px}
.return-pct{position:absolute;left:0;right:0;bottom:5px;font-size:8px;line-height:10px}
</style>
</head>
<body>
<div class="stage">

  <section class="slide s1">
    <div class="cover-band">
      <h1 class="cover-title">Project Title Here</h1>
      <p class="cover-sub">Lorem ipsum dolor sit ipsum Lorem ipsum dolor sit ipsum Lorem ipsum dolor sit ipsum Lorem ipsum dolor sit ipsum</p>
    </div>
    <div class="brand"><div class="brand-square"></div><div class="brand-name">Harrowgate Capital</div></div>
  </section>

  <section class="slide s2">
    <h2 class="slide-title"><span>About Us</span></h2>
    <div class="item" style="top:64px;width:272px">
      <div class="item-icon"></div>
      <div>
        <h3>Subtitle Here</h3>
        <p>Lorem ipsum dolor sit ipsum Lorem ipsum dolor sit ipsum Lorem ipsum dolor sit ipsum Lorem ipsum dolor sit ipsum Lorem ipsum dolor sit ipsum Lorem ipsum dolor sit ipsum</p>
        <p>Lorem ipsum dolor sit ipsum Lorem ipsum dolor sit ipsum Lorem ipsum dolor sit ipsum Lorem ipsum dolor sit ipsum Lorem ipsum dolor sit ipsum Lorem ipsum dolor sit ipsum</p>
        <p>Lorem ipsum dolor sit ipsum Lorem ipsum dolor sit ipsum Lorem ipsum dolor sit ipsum Lorem ipsum dolor sit ipsum Lorem ipsum dolor sit ipsum Lorem ipsum dolor sit ipsum</p>
      </div>
    </div>
    <div class="photo photo-towers" role="img" aria-label="Glass office towers seen from below against a blue sky"></div>
  </section>

  <section class="slide s3">
    <h2 class="slide-title"><span style="padding:0 2px 1px">Market Snapshot</span></h2>
    <svg class="abs" style="left:0;top:0" width="520" height="389" viewBox="0 0 520 389">
      <g class="chart-label" font-size="5.5" font-weight="700" fill="#333">
        <text x="183" y="67">2%</text>
        <text x="286" y="67">% OF STOCK</text>
        <text x="407" y="67">5%</text>
        <text x="105" y="178" font-weight="400">m sq ft</text>
        <text x="124" y="130">0</text>
        <text x="124" y="225">3</text>
      </g>
      <line x1="180" y1="70" x2="420" y2="70" stroke="var(--bar)" stroke-width="1"/>
      <path d="M420 67 L425 70 L420 73Z" fill="var(--bar)"/>
      <line x1="128" y1="128" x2="430" y2="128" stroke="#999" stroke-width=".6"/>
      <line x1="128" y1="223" x2="430" y2="223" stroke="#999" stroke-width=".6"/>
      <g fill="var(--bar)">
        <rect x="183" y="128" width="21" height="16"/>
        <rect x="208" y="128" width="21" height="13"/>
        <rect x="233" y="128" width="20" height="29"/>
        <rect x="258" y="128" width="20" height="10"/>
        <rect x="283" y="128" width="20" height="6"/>
        <rect x="308" y="128" width="20" height="10"/>
        <rect x="333" y="128" width="20" height="73"/>
        <rect x="357" y="128" width="21" height="82"/>
        <rect x="382" y="128" width="21" height="13"/>
        <rect x="407" y="128" width="21" height="6"/>
      </g>
      <g class="chart-label" font-size="8" font-weight="600" fill="var(--bar-label)">
        <text x="183" y="153">0.5m</text><text x="208" y="150">0.4m</text>
        <text x="233" y="165">0.9m</text><text x="258" y="146">0.3m</text>
        <text x="283" y="143">0.2m</text><text x="308" y="146">0.3m</text>
        <text x="333" y="209">2.3m</text><text x="358" y="218">2.6m</text>
        <text x="382" y="150">0.4m</text><text x="407" y="142">0.2m</text>
      </g>
      <g class="chart-label" font-size="5" font-weight="700" fill="#333">
        <text transform="translate(191,156) rotate(90)">EDINBURGH</text>
        <text transform="translate(216,153) rotate(90)">GLASGOW</text>
        <text transform="translate(240,170) rotate(90)">MANCHESTER</text>
        <text transform="translate(266,150) rotate(90)">MIDTOWN</text>
        <text transform="translate(291,146) rotate(90)">UXBRIDGE</text>
        <text transform="translate(316,150) rotate(90)">CAMBRIDGE</text>
        <text transform="translate(341,213) rotate(90)">CITY</text>
        <text transform="translate(366,223) rotate(90)">WEST END</text>
        <text transform="translate(391,152) rotate(90)">READING</text>
        <text transform="translate(416,145) rotate(90)">STAINES</text>
      </g>
      <text class="chart-label" x="266" y="269" text-anchor="middle" font-size="6.5" font-weight="700" fill="var(--red)">2014 TOTAL RETURNS (% PA)</text>
    </svg>
    <div class="return" style="left:93px"><div class="return-name">Rest of the UK</div><div class="return-pct">16.9%</div></div>
    <div class="return" style="left:181px"><div class="return-name">City</div><div class="return-pct">20.2%</div></div>
    <div class="return" style="left:269px"><div class="return-name">South East</div><div class="return-pct">22.5%</div></div>
    <div class="return" style="left:357px"><div class="return-name" style="top:3px">West End<br>&amp; Midtown</div><div class="return-pct">24.0%</div></div>
  </section>

  <section class="slide s4">
    <h2 class="slide-title"><span>About Us</span></h2>
    <div class="item" style="top:65px;width:482px">
      <div class="item-icon"></div>
      <div><h3>Subtitle Here</h3><p>Lorem ipsum dolor sit ipsum Lorem ipsum dolor sit ipsum Lorem ipsum dolor sit ipsum Lorem ipsum dolor sit ipsum Lorem ipsum dolor sit ipsum Lorem ipsum dolor sit ipsum Lorem ipsum dolor sit ipsum</p></div>
    </div>
    <div class="item" style="top:127px;width:482px">
      <div class="item-icon"></div>
      <div><h3>Subtitle Here</h3><p>Lorem ipsum dolor sit ipsum Lorem ipsum dolor sit ipsum Lorem ipsum dolor sit ipsum Lorem ipsum dolor sit ipsum Lorem ipsum dolor sit ipsum Lorem ipsum dolor sit ipsum Lorem ipsum dolor sit ipsum</p></div>
    </div>
    <div class="item" style="top:190px;width:482px">
      <div class="item-icon"></div>
      <div><h3>Subtitle Here</h3><p>Lorem ipsum dolor sit ipsum Lorem ipsum dolor sit ipsum Lorem ipsum dolor sit ipsum Lorem ipsum dolor sit ipsum Lorem ipsum dolor sit ipsum Lorem ipsum dolor sit ipsum Lorem ipsum dolor sit ipsum</p></div>
    </div>
    <div class="item" style="top:252px;width:482px">
      <div class="item-icon"></div>
      <div><h3>Subtitle Here</h3><p>Lorem ipsum dolor sit ipsum Lorem ipsum dolor sit ipsum Lorem ipsum dolor sit ipsum Lorem ipsum dolor sit ipsum Lorem ipsum dolor sit ipsum Lorem ipsum dolor sit ipsum Lorem ipsum dolor sit ipsum dolor sit ipsumsit ipsum Lorem ipsum dolor sit ipsum</p></div>
    </div>
  </section>

  <section class="slide s5 tall">
    <h2 class="slide-title"><span>About Us</span></h2>
    <div class="image-band">Image Title Here</div>
    <div class="photo photo-river" role="img" aria-label="City skyline with a tall spire above a river and bridge at sunset"></div>
    <div class="column">
      <p>Lorem ipsum dolor sit ipsum Lorem ipsum dolor sit ipsum Lorem ipsum dolor sit ipsum Lorem ipsum dolor sit ipsum Lorem ipsum dolor sit ipsum Lorem ipsum dolor sit ipsum</p>
      <p>Lorem ipsum dolor sit ipsum Lorem ipsum dolor sit ipsum Lorem ipsum dolor sit ipsum Lorem ipsum dolor sit ipsum Lorem ipsum dolor sit ipsum Lorem ipsum dolor sit ipsum Lorem ipsum dolor sit ipsum Lorem ipsum dolor sit ipsum Lorem ipsum dolor sit ipsum Lorem ipsum dolor sit ipsum</p>
      <p>Lorem ipsum dolor sit ipsum Lorem ipsum dolor sit ipsum Lorem ipsum dolor sit ipsum Lorem ipsum dolor sit ipsum</p>
      <p>Lorem ipsum dolor sit ipsum Lorem ipsum dolor sit ipsum Lorem ipsum dolor sit ipsum Lorem ipsum dolor sit ipsum</p>
    </div>
  </section>

  <section class="slide s6 tall">
    <div class="header-band">Project Title Here</div>
    <div class="image-band light">Image Title Here</div>
    <div class="photo photo-river" role="img" aria-label="City skyline with a tall spire above a river and bridge at sunset"></div>
    <div class="column">
      <p>Lorem ipsum dolor sit ipsum Lorem ipsum dolor sit ipsum Lorem ipsum dolor sit ipsum Lorem ipsum dolor sit ipsum Lorem ipsum dolor sit ipsum Lorem ipsum dolor sit ipsum</p>
      <p>Lorem ipsum dolor sit ipsum Lorem ipsum dolor sit ipsum Lorem ipsum dolor sit ipsum Lorem ipsum dolor sit ipsum Lorem ipsum dolor sit ipsum Lorem ipsum dolor sit ipsum Lorem ipsum dolor sit ipsum Lorem ipsum dolor sit ipsum Lorem ipsum dolor sit ipsum Lorem ipsum dolor sit ipsum</p>
      <p>Lorem ipsum dolor sit ipsum Lorem ipsum dolor sit ipsum Lorem ipsum dolor sit ipsum Lorem ipsum dolor sit ipsum</p>
      <p>Lorem ipsum dolor sit ipsum Lorem ipsum dolor sit ipsum Lorem ipsum dolor sit ipsum Lorem ipsum dolor sit ipsum</p>
    </div>
  </section>

</div>
</body>
</html>
```